Cover for a Non-Fiction Book on Authoritarianism for a Washington D.C. Think Tank

Create a dynamic and engaging cover highlighting the role of contemporary and historical authoritarianism for a non-fiction edited volume. The book brings together chapters from many leading academics on the subject. The tone should be serious but provocative. Proprietary images are not acceptable as we are not budgeting for licensing. The books dimensions are 6x9. Preference will be given to designers with front and back cover design with sample ipsum lorum text.

One of covers that we particularly liked was "How Quiet Defiance Endures" a link to the image on shelvoria is: http://www.shelvoria-books.example/s/ref=nb_sb_noss/482-7715093-6620841?url=search-alias%3Daps&field-keywords=How+Quiet+Defiance+Endures

Attached is a draft version of the manuscript to assist in shaping your creative vision.

Project Deadline Extended Reason: I have extended the deadline at the request of the editors. They would like to see some designs that rely less heavily on the themes of fists and barbed wire to reference authoritarianism. I apologize to designs with current submissions, some of them are very professional, however none of the designs are currently under consideration for use. Added Saturday, January 24, 2015

Project Deadline Extended Reason: Editors are still unsatisfied with current sample of options. I apologize to those current contributors, but anything challenging and new would be well received. Added Friday, January 30, 2015

Project Deadline Extended Reason: I've updated the deadline so that designers that were well ranked can submit full front and back covers to assist the book editors in making their final decision. Added Friday, February 13, 2015

Font styles to use
Serif
Sans Serif

Requirements
Must have
• 1) Title: Are Strongmen Regaining the Upper Ground
• 2) Editors: Tobias Lindqvern and Elena K. Marwood
• 3) Language from client: "a simple design that captured both a symbol of repression and resistance would be ideal. The cover of How Quiet Defiance Endures is a great example. Nothing busy or overly complicated. The image of mass street protests may be overused at this point so I'd opt for something a bit more creative. Vibrant colors always great."
• 4) This final project design must use the attached InDesign template file when constructing the cover (IDML and INDD versions of the template are available).
Nice to have
• Feel free to use Harborline Forum logo designs pulled from the web.
Should not have
• Photographs that would require compensating a copyright holder.

```html
<!DOCTYPE html>
<html lang="en">
<head>
<meta charset="utf-8">
<title>Are Strongmen Regaining the Upper Ground — Book Cover</title>
<link rel="stylesheet" href="https://fonts.googleapis.com/css2?family=Anton&family=Bebas+Neue&display=swap">
<style>
  :root {
    --stage: #dcdcdc;
    --paper: #f6f3e2;
    --signal-red: #e0473f;
    --deep-red: #a8403a;
    --ink: #2a2626;
    --cream-type: #f6f3e2;
  }
  html, body {
    margin: 0;
    padding: 0;
    width: 1200px;
    height: 1049px;
    overflow: hidden;
    background: var(--stage);
  }
  .canvas {
    position: relative;
    width: 1200px;
    height: 1049px;
  }
  .cover {
    position: absolute;
    left: 300px;
    top: 74px;
    width: 600px;
    height: 900px;
    background: var(--paper);
  }
  .key-art {
    position: absolute;
    left: 105px;
    top: 94px;
    width: 390px;
    height: 506px;
    background: linear-gradient(180deg, var(--deep-red) 0%, var(--signal-red) 45%, var(--signal-red) 100%);
  }
  .title {
    position: absolute;
    left: 105px;
    top: 262px;
    width: 390px;
    margin: 0;
    text-align: center;
    font-weight: 400;
    color: var(--ink);
  }
  .title-line {
    display: block;
    font-family: "Bebas Neue", sans-serif;
    white-space: nowrap;
  }
  .title-line--small {
    font-size: 38px;
    line-height: 38px;
  }
  .title-line--heavy {
    font-family: "Anton", sans-serif;
    font-size: 62px;
    line-height: 72px;
  }
  .title-line--mid {
    font-size: 48px;
    line-height: 46px;
  }
  .title-line--light {
    color: var(--cream-type);
    font-size: 34px;
    line-height: 40px;
    letter-spacing: 14px;
    padding-left: 14px;
  }
  .title-line--base {
    font-family: "Anton", sans-serif;
    font-size: 100px;
    line-height: 112px;
  }
  .editors {
    position: absolute;
    left: 0;
    right: 0;
    top: 772px;
    margin: 0;
    text-align: center;
    font-family: "Bebas Neue", sans-serif;
    font-size: 27px;
    line-height: 24px;
    letter-spacing: 0.5px;
    color: var(--ink);
  }
  .editors .editor {
    display: block;
  }
  .editors .accent {
    color: var(--signal-red);
  }
</style>
</head>
<body>
  <main class="canvas">
    <article class="cover">
      <div class="key-art" role="img" aria-label="Cover illustration: a watching eye above a red pyramid, symbol of surveillance and power"></div>
      <h1 class="title">
        <span class="title-line title-line--small">Are</span>
        <span class="title-line title-line--heavy">STRONGMEN</span>
        <span class="title-line title-line--mid">Regaining</span>
        <span class="title-line title-line--light">THE UPPER</span>
        <span class="title-line title-line--base">GROUND</span>
      </h1>
      <p class="editors">
        <span class="editor"><span class="accent">Tobias</span> Lindqvern</span>
        <span class="editor">Elena K. <span class="accent">Marwood</span></span>
      </p>
    </article>
  </main>
</body>
</html>
```